Cyber Security Site Design (Products & Consulting)

I need my website redesigned to be engaging, clean, efficient and modern. My company (when its up and running) is going to be concentrated on two things: a few specific products for cyber security as well as cyber security consulting services. The background I bring to the field is having worked with small companies all the way to the largest government organizations and advising them on their security posture and how to improve it. We need the ability to add products and services easily.

For a sample product, you can use either Tarnel (http://www.tarnel-relay.org/) or Vornidex Graywell (https://www.vornidex.com/products/relay-kx-and-enhanced-safe-portal).

It will replace https://dalmorenvue.com/

Target Market(s)

Cyber Security professionals in all verticals

Coding

Coded - Design and coding required

Number of Pages Required

4 page

Font styles to use
Sans Serif

Colors
6b449b

Requirements
Must have
• Ability to easily modify
• Have main page
• Have product specific pages
• Have consulting services pages
• Have executive team information
• Clean, modern design
• Usage of the logo and its color scheme
Nice to have
• I like the idea of a left collapsed sidebar (so icons only) that can expand for text.
• I am also open to a very unique landing page, possibly a shape in the middle (hexagons maybe?) with each of the options there.
Should not have
• Nothing that looks like it came out of a hacker movie

```html
<!DOCTYPE html>
<html lang="en">
<head>
<meta charset="utf-8">
<title>Dalmoren Vue — Cyber Security Consulting</title>
<link rel="stylesheet" href="https://fonts.googleapis.com/css2?family=Roboto:wght@400;500;700;900&display=swap">
<style>
:root{
  --purple:#6b449b;
  --purple-dark:#5a3888;
  --ink:#1d1d1f;
  --text:#3a3a3a;
  --muted:#8a8a8a;
  --dark:#262626;
  --darker:#1c1c1c;
  --light:#f3f1f3;
  --white:#ffffff;
  --line:#e3e3e3;
}
*{box-sizing:border-box;margin:0;padding:0}
html,body{width:1200px;height:3462px;overflow:hidden}
body{font-family:"Roboto",Arial,sans-serif;color:var(--text);background:var(--white);position:relative}
.block{position:absolute;left:0;width:1200px}
.abs{position:absolute}

/* top bar */
.topbar{top:0;height:32px;background:var(--dark)}
.topbar__left{left:0;top:0;width:600px;height:32px;background:var(--white);clip-path:polygon(0 0,100% 0,96% 100%,0 100%)}
.topbar__purple{left:560px;top:0;width:60px;height:32px;background:var(--purple);clip-path:polygon(70% 0,100% 0,33% 100%,0 100%)}
.social{display:flex;gap:6px}
.social span{width:14px;height:14px;border-radius:2px;background:var(--purple)}
.topbar .social{left:173px;top:9px}
.search{left:712px;top:5px;width:166px;height:22px;border-radius:11px;background:var(--white);font-size:9px;font-weight:700;color:var(--purple);padding:6px 0 0 14px}
.search i{position:absolute;right:2px;top:2px;width:18px;height:18px;border-radius:50%;background:var(--purple)}
.cart{left:890px;top:5px;width:138px;height:22px;border-radius:11px;background:var(--purple);color:var(--white);font-size:8.5px;font-weight:500;padding:6px 0 0 28px;white-space:nowrap}

/* header */
.header{top:32px;height:98px;background:var(--white)}
.logo{left:173px;top:18px;display:flex;align-items:center;gap:10px}
.logo__mark{width:40px;height:40px;background:var(--purple);border-radius:6px}
.logo__name{font-size:34px;font-weight:500;color:var(--purple);letter-spacing:1px;line-height:1}
.logo__tag{font-size:11px;letter-spacing:6px;color:var(--purple);margin-top:3px}
.info{display:flex;gap:12px;top:30px}
.info svg{flex:none}
.info h4{font-size:12px;font-weight:700;color:var(--ink);margin-bottom:3px}
.info p{font-size:10.5px;color:var(--text)}
.nav{top:130px;height:40px;border-top:1px solid var(--line);background:var(--white)}
.nav ul{list-style:none;position:absolute;left:352px;top:0;display:flex;gap:48px}
.nav li{font-size:11px;font-weight:700;color:var(--ink);padding-top:13px;height:40px}
.nav li.is-active{color:var(--purple);border-top:3px solid var(--purple);padding-top:10px;margin-top:-1px}

/* hero */
.hero{top:170px;height:552px;overflow:hidden}
.hero__photo{left:0;top:0;width:1200px;height:552px;
  background:
    radial-gradient(ellipse 300px 170px at 1000px 70px,rgba(222,224,228,.95) 0,rgba(170,173,178,.7) 45%,rgba(0,0,0,0) 100%),
    radial-gradient(ellipse 260px 300px at 790px 330px,rgba(120,112,106,.75) 0,rgba(0,0,0,0) 100%),
    radial-gradient(ellipse 380px 260px at 300px 110px,rgba(150,146,140,.55) 0,rgba(0,0,0,0) 100%),
    radial-gradient(ellipse 420px 260px at 1080px 480px,rgba(30,31,34,.9) 0,rgba(0,0,0,0) 100%),
    linear-gradient(110deg,#7a7874 0%,#55565a 38%,#3a3b3f 62%,#26272a 100%)}
.hero__panel{left:108px;top:146px;width:382px;height:240px;background:rgba(120,110,95,.35)}
.hero__kicker{left:173px;top:196px;font-size:17px;font-weight:500;color:var(--white)}
.hero__title{left:173px;top:224px;font-size:32px;font-weight:900;line-height:1.06;color:var(--white)}
.btn{display:inline-block;background:var(--purple);color:var(--white);font-size:11px;font-weight:700;text-align:center}
.hero .btn{left:173px;top:326px;width:112px;height:37px;padding-top:12px}
.arrow{width:26px;height:26px;border-radius:50%;background:rgba(0,0,0,.55);top:233px}

/* section heads */
.kicker{width:1200px;text-align:center;font-size:13px;font-weight:700;color:var(--purple)}
.title{width:1200px;text-align:center;font-size:35px;font-weight:900;color:var(--ink);letter-spacing:-.5px}
.divider{width:1200px;display:flex;justify-content:center}
.lead{left:220px;width:760px;text-align:center;font-size:11.5px;line-height:1.6;color:var(--text)}

/* services */
.services{top:722px;height:425px;background:var(--white)}
.card{top:220px;width:272px;height:136px;border:1px solid var(--line);background:var(--white);box-shadow:0 14px 24px -14px rgba(0,0,0,.18);padding:24px 18px 0 20px;display:flex;gap:14px}
.card svg{flex:none;margin-top:12px}
.card h3{font-size:12.5px;font-weight:700;color:var(--ink);margin-bottom:8px}
.card p{font-size:10.5px;line-height:1.55;text-align:justify}

/* about */
.about{top:1147px;height:485px}
.about__left{left:0;top:0;width:605px;height:485px;background:var(--purple)}
.about__right{left:605px;top:0;width:595px;height:485px;background:var(--dark)}
.about__photo{left:651px;top:49px;width:372px;height:383px;background:var(--white);padding:6px}
.about__photo div{width:100%;height:100%;
  background:
    radial-gradient(ellipse 130px 150px at 50% 34%,rgba(214,170,140,.85) 0,rgba(214,170,140,0) 100%),
    radial-gradient(ellipse 220px 120px at 50% 100%,rgba(52,54,60,1) 0,rgba(52,54,60,.6) 60%,rgba(52,54,60,0) 100%),
    linear-gradient(180deg,#f1f1f3 0%,#e6e6ea 45%,#7c7f88 80%,#3d3f46 100%)}
.about .kicker{left:173px;width:auto;text-align:left;color:var(--white);top:78px}
.about .title{left:173px;width:auto;text-align:left;color:var(--white);top:96px}
.about p.copy{left:173px;top:180px;width:390px;font-size:11.5px;line-height:1.55;color:var(--white);text-align:justify}
.contact{top:290px;display:flex;gap:10px;color:var(--white)}
.contact h4{font-size:11.5px;font-weight:700}
.contact p{font-size:11.5px}
.btn--ghost{left:173px;top:376px;width:124px;height:42px;border:1px solid var(--white);background:transparent;padding-top:14px}

/* products */
.products{top:1632px;height:545px;background:var(--light)}
.product{top:201px;width:272px;text-align:center}
.product__img{height:150px}
.product h3{font-size:13px;font-weight:900;color:var(--ink);margin:18px 0 8px}
.product p{font-size:10.5px;line-height:1.6;padding:0 2px}
.product .btn{width:110px;height:33px;padding-top:11px;margin-top:12px}

/* clients */
.clients{top:2177px;height:392px}
.clients__photo{left:0;top:0;width:588px;height:392px;
  background:
    radial-gradient(ellipse 200px 140px at 110px 300px,rgba(70,72,78,.55) 0,rgba(0,0,0,0) 100%),
    radial-gradient(ellipse 160px 200px at 520px 230px,rgba(60,64,72,.6) 0,rgba(0,0,0,0) 100%),
    radial-gradient(ellipse 260px 140px at 300px 40px,rgba(250,250,250,.9) 0,rgba(0,0,0,0) 100%),
    linear-gradient(120deg,#e4e7ea 0%,#c4cad0 45%,#99a1a8 100%)}
.clients__dark{left:588px;top:0;width:612px;height:392px;background:var(--darker)}
.quote{left:173px;top:85px;width:312px;height:222px;background:var(--white);text-align:center;padding:64px 34px 0}
.quote__mark{left:126px;top:-18px}
.quote p{font-size:10.5px;line-height:1.6}
.quote h5{font-size:10px;font-weight:700;color:var(--ink);margin-top:14px}
.quote h5 em{font-style:normal;color:var(--purple);font-size:8.5px}
.clients__title{left:614px;top:78px;font-size:33px;font-weight:900;color:var(--white)}
.clients__text{left:614px;top:165px;width:420px;font-size:11.5px;line-height:1.6;color:var(--white)}
.badge{top:228px;width:80px;height:74px;border:1px solid #3a3a3a;display:flex;align-items:center;justify-content:center}

/* team */
.team{top:2569px;height:570px;background:var(--white)}
.member{top:194px;width:198px;text-align:center}
.member__photo{height:256px}
.member h4{font-size:13px;font-weight:700;color:var(--ink);margin-top:24px}
.member p{font-size:11px;color:var(--muted);margin-top:6px}
.member__over{position:absolute;left:0;top:0;width:198px;height:256px;background:rgba(30,30,30,.78);color:var(--white);padding-top:80px}
.member__over h4{color:var(--white);margin:0;font-size:14px}
.member__over p{color:var(--white);margin:4px 0 10px}
.member__over .social{justify-content:center}
.member__over .social span{background:var(--white)}

/* footer */
.footer{top:3139px;height:265px;background:var(--darker);color:var(--white)}
.footer h3{font-size:21px;font-weight:700;top:38px}
.footer p{font-size:10px;line-height:1.6}
.news{display:flex;gap:14px}
.date{flex:none;width:32px;height:36px;background:#333;text-align:center;font-size:11px;font-weight:700;padding-top:4px;line-height:1.2}
.date small{display:block;font-size:8px}
.news em{font-style:normal;font-size:9px;display:block}
.addr{display:grid;grid-template-columns:95px 1fr;row-gap:22px;font-size:10px;line-height:1.6}
.footer .social span{background:var(--white);width:18px;height:18px}
.bottombar{top:3404px;height:58px;background:var(--purple);color:var(--white)}
.bottombar p{left:173px;top:22px;font-size:10px}
.bottombar ul{list-style:none;position:absolute;right:173px;top:22px;display:flex;gap:18px;font-size:10px}
</style>
</head>
<body>

<!-- top bar -->
<div class="block topbar">
  <div class="abs topbar__left"></div>
  <div class="abs topbar__purple"></div>
  <div class="abs social"><span></span><span></span><span></span><span></span><span></span></div>
  <div class="abs search">SEARCH HERE<i></i></div>
  <div class="abs cart">CART: 0 ITEMS - $0.00</div>
</div>

<!-- header -->
<header class="block header">
  <div class="abs logo">
    <span class="logo__mark"></span>
    <div><div class="logo__name">DALMOREN</div><div class="logo__tag">VUE</div></div>
  </div>
  <div class="abs info" style="left:452px">
    <svg width="34" height="34" viewBox="0 0 34 34" fill="none" stroke="#6b449b" stroke-width="2"><circle cx="17" cy="17" r="14"/><path d="M17 9v8l6 4"/></svg>
    <div><h4>WORKING HOURS</h4><p>Monday-Sunday : 8:00 am to 10:30 pm</p></div>
  </div>
  <div class="abs info" style="left:700px">
    <svg width="26" height="34" viewBox="0 0 26 34" fill="none" stroke="#6b449b" stroke-width="2"><rect x="5" y="2" width="16" height="30" rx="3"/><path d="M11 27h4"/></svg>
    <div><h4>PHONE</h4><p>+440 870555214</p></div>
  </div>
  <div class="abs info" style="left:848px">
    <svg width="34" height="30" viewBox="0 0 34 30" fill="none" stroke="#6b449b" stroke-width="2"><rect x="2" y="5" width="30" height="20"/><path d="M2 5l15 12 15-12"/></svg>
    <div><h4>MAIL</h4><p>info@dalmorenvue.com</p></div>
  </div>
</header>

<nav class="block nav">
  <ul><li class="is-active">HOME</li><li>OUR TEAM</li><li>SERVICES</li><li>PRODUCT</li><li>CONTACT US</li></ul>
</nav>

<!-- hero -->
<section class="block hero">
  <div class="abs hero__photo" role="img" aria-label="Photo of hands holding a smartphone showing a padlock, with a laptop keyboard behind and network icons around it"></div>
  <div class="abs hero__panel"></div>
  <p class="abs hero__kicker">THE MOST SUCCESSFUL</p>
  <h1 class="abs hero__title">CYBER SECURITY<br>CONSULTING SERVICES</h1>
  <span class="abs btn">READ MORE</span>
  <span class="abs arrow" style="left:30px"></span>
  <span class="abs arrow" style="left:1120px"></span>
</section>

<!-- services -->
<section class="block services">
  <p class="abs kicker" style="top:48px">SERVICES TO</p>
  <h2 class="abs title" style="top:64px">DALMOREN VUE</h2>
  <div class="abs divider" style="top:108px">
    <svg width="86" height="16" viewBox="0 0 86 16"><path d="M0 11h32M54 11h32" stroke="#6b449b" stroke-width="2"/><rect x="37" y="6" width="12" height="9" fill="#6b449b"/><path d="M39.5 7V4a3.5 3.5 0 017 0v3" fill="none" stroke="#6b449b" stroke-width="1.6"/></svg>
  </div>
  <p class="abs lead" style="top:140px">Lorem Ipsum is simply dummy text of the printing and typesetting industry. Lorem Ipsum has been the industry's standard dummy text ever since the 1500s, when an unknown printer took a galley of type and scrambled it.</p>

  <div class="abs card" style="left:173px">
    <svg width="58" height="56" viewBox="0 0 58 56" fill="none" stroke="#6b449b" stroke-width="2.5"><rect x="6" y="22" width="22" height="18" fill="#6b449b"/><path d="M10 22v-6a7 7 0 0114 0v6"/><path d="M28 31h10l6-10h8M38 31l6 10h8M28 31h24"/><circle cx="52" cy="21" r="3"/><circle cx="52" cy="41" r="3"/></svg>
    <div><h3>INFORMATION SECURITY</h3><p>Lorem Ipsum is simply dummy text of the printing and typesetting industry.</p></div>
  </div>
  <div class="abs card" style="left:466px">
    <svg width="58" height="56" viewBox="0 0 58 56" fill="none" stroke="#6b449b" stroke-width="2.5"><rect x="4" y="8" width="50" height="32"/><rect x="8" y="12" width="42" height="24" fill="#6b449b"/><path d="M22 48h14M29 40v8"/><circle cx="29" cy="24" r="6" fill="#fff" stroke="none"/></svg>
    <div><h3>THREAT PROTECT</h3><p>Lorem Ipsum is simply dummy text of the printing and typesetting industry.</p></div>
  </div>
  <div class="abs card" style="left:757px">
    <svg width="58" height="56" viewBox="0 0 58 56" fill="none" stroke="#6b449b" stroke-width="2.5"><rect x="12" y="4" width="40" height="30"/><path d="M12 4l20 15 20-15"/><rect x="4" y="28" width="22" height="20" fill="#6b449b"/><path d="M2 52h28"/></svg>
    <div><h3>EMAIL SECURITY</h3><p>Lorem Ipsum is simply dummy text of the printing and typesetting industry.</p></div>
  </div>
</section>

<!-- about -->
<section class="block about">
  <div class="abs about__left"></div>
  <div class="abs about__right"></div>
  <p class="abs kicker">SHORTLY</p>
  <h2 class="abs title">ABOUT US</h2>
  <div class="abs" style="left:173px;top:140px">
    <svg width="86" height="16" viewBox="0 0 86 16"><path d="M0 11h32M54 11h32" stroke="#fff" stroke-width="2"/><rect x="37" y="6" width="12" height="9" fill="#fff"/><path d="M39.5 7V4a3.5 3.5 0 017 0v3" fill="none" stroke="#fff" stroke-width="1.6"/></svg>
  </div>
  <p class="abs copy">Lorem Ipsum is simply dummy text of the printing and typesetting industry. Lorem Ipsum has been the industry's standard dummy text ever since the 1500s, when an unknown printer took a galley of type and scrambled it. Lorem Ipsum is simply dummy text of the printing and typesetting industry.</p>
  <div class="abs contact" style="left:173px">
    <svg width="34" height="34" viewBox="0 0 34 34" fill="none" stroke="#fff" stroke-width="1.5"><circle cx="17" cy="17" r="16"/><path d="M12 10l3 0 2 4-2 2a10 10 0 004 4l2-2 4 2v3c-8 1-15-6-14-13z"/></svg>
    <div><h4>PHONE</h4><p>+440 870555214</p></div>
  </div>
  <div class="abs contact" style="left:348px">
    <svg width="34" height="34" viewBox="0 0 34 34" fill="none" stroke="#fff" stroke-width="1.5"><circle cx="17" cy="17" r="16"/><rect x="9" y="11" width="16" height="12"/><path d="M9 11l8 7 8-7"/></svg>
    <div><h4>MAIL</h4><p>info@dalmorenvue.com</p></div>
  </div>
  <span class="abs btn btn--ghost">READ MORE</span>
  <div class="abs about__photo"><div role="img" aria-label="Portrait photo of the company founder in a dark suit and checked shirt on a light background"></div></div>
</section>

<!-- products -->
<section class="block products">
  <p class="abs kicker" style="top:54px">WE OFFER FOR DOWNLOAD</p>
  <h2 class="abs title" style="top:72px">OUR PRODUCT</h2>
  <div class="abs divider" style="top:116px">
    <svg width="86" height="16" viewBox="0 0 86 16"><path d="M0 11h32M54 11h32" stroke="#6b449b" stroke-width="2"/><rect x="37" y="6" width="12" height="9" fill="#6b449b"/><path d="M39.5 7V4a3.5 3.5 0 017 0v3" fill="none" stroke="#6b449b" stroke-width="1.6"/></svg>
  </div>
  <p class="abs lead" style="top:143px">Lorem Ipsum is simply dummy text of the printing and typesetting industry. Lorem Ipsum has been the industry's standard dummy text ever since the 1500s, when an unknown printer took a galley of type and scrambled it.</p>

  <div class="abs product" style="left:173px">
    <div class="product__img" role="img" aria-label="Blue digital padlock over a circuit network" style="background:radial-gradient(ellipse 90px 70px at 50% 50%,rgba(170,220,255,.85) 0,rgba(60,140,230,.4) 55%,rgba(0,0,0,0) 100%),radial-gradient(ellipse 120px 60px at 15% 85%,rgba(90,170,255,.5) 0,rgba(0,0,0,0) 100%),linear-gradient(135deg,#0b2a6e,#2467c4 55%,#071845)"></div>
    <h3>LOREM IPSUM IS SIMPLY</h3>
    <p>Lorem Ipsum is simply dummy text of the printing and typesetting industry. Lorem Ipsum has been the industry's standard dummy text ever since the .</p>
    <span class="btn">SHOP NOW</span>
  </div>
  <div class="abs product" style="left:466px">
    <div class="product__img" role="img" aria-label="Hand touching a glowing padlock on a dark blue screen" style="background:radial-gradient(ellipse 70px 60px at 55% 65%,rgba(190,230,245,.8) 0,rgba(70,150,190,.35) 60%,rgba(0,0,0,0) 100%),radial-gradient(ellipse 120px 80px at 75% 15%,rgba(120,140,160,.45) 0,rgba(0,0,0,0) 100%),linear-gradient(135deg,#0c2233,#24607e 55%,#08141e)"></div>
    <h3>LOREM IPSUM IS SIMPLY</h3>
    <p>Lorem Ipsum is simply dummy text of the printing and typesetting industry. Lorem Ipsum has been the industry's standard dummy text ever since the .</p>
    <span class="btn">SHOP NOW</span>
  </div>
  <div class="abs product" style="left:757px">
    <div class="product__img" role="img" aria-label="Person typing on a laptop with security lock icons overlaid" style="background:radial-gradient(ellipse 110px 70px at 70% 35%,rgba(190,250,255,.85) 0,rgba(80,200,220,.4) 55%,rgba(0,0,0,0) 100%),radial-gradient(ellipse 110px 80px at 20% 80%,rgba(30,50,70,.7) 0,rgba(0,0,0,0) 100%),linear-gradient(135deg,#2a6f8a,#4fbdd4 55%,#1d3446)"></div>
    <h3>LOREM IPSUM IS SIMPLY</h3>
    <p>Lorem Ipsum is simply dummy text of the printing and typesetting industry. Lorem Ipsum has been the industry's standard dummy text ever since the .</p>
    <span class="btn">SHOP NOW</span>
  </div>
</section>

<!-- clients -->
<section class="block clients">
  <div class="abs clients__photo" role="img" aria-label="Office meeting room with colleagues around a table and screens on the wall"></div>
  <span class="abs arrow" style="left:88px;top:183px"></span>
  <span class="abs arrow" style="left:528px;top:183px"></span>
  <div class="abs quote">
    <svg class="abs quote__mark" width="60" height="50" viewBox="0 0 60 50"><path d="M10 10h16l-8 34H4zM36 10h16l-8 34H30z" fill="#6b449b"/></svg>
    <p>Lorem Ipsum is simply dummy text of the printing and typesetting industry. Lorem Ipsum has been the industry's standard dummy text ever since the 1500s, when an unknown printer took a galley of type and scrambled it.</p>
    <h5>MAREK OLIN <em>- Developer</em></h5>
  </div>
  <div class="abs clients__dark"></div>
  <h2 class="abs clients__title">CLIENT &amp; PARTNER</h2>
  <div class="abs" style="left:614px;top:130px">
    <svg width="86" height="16" viewBox="0 0 86 16"><path d="M0 11h32M54 11h32" stroke="#fff" stroke-width="2"/><rect x="37" y="6" width="12" height="9" fill="#fff"/><path d="M39.5 7V4a3.5 3.5 0 017 0v3" fill="none" stroke="#fff" stroke-width="1.6"/></svg>
  </div>
  <p class="abs clients__text">Lorem Ipsum is simply dummy text of the printing and typesetting industry. Lorem Ipsum has been the industry's standard dummy text ever .</p>
  <div class="abs badge" style="left:614px"><span style="font-size:9px;font-weight:500;color:#9a9a9a">PALECREST</span></div>
  <div class="abs badge" style="left:702px"><svg width="40" height="40"><rect x="8" y="8" width="24" height="24" fill="none" stroke="#8a8a8a" stroke-width="1.5"/></svg></div>
  <div class="abs badge" style="left:789px"><svg width="40" height="40"><circle cx="20" cy="20" r="14" fill="none" stroke="#8a8a8a" stroke-width="1.5"/></svg></div>
</section>

<!-- team -->
<section class="block team">
  <p class="abs kicker" style="top:46px">EXPERT MEMBERS</p>
  <h2 class="abs title" style="top:64px">OUR TEAM</h2>
  <div class="abs divider" style="top:108px">
    <svg width="86" height="16" viewBox="0 0 86 16"><path d="M0 11h32M54 11h32" stroke="#6b449b" stroke-width="2"/><rect x="37" y="6" width="12" height="9" fill="#6b449b"/><path d="M39.5 7V4a3.5 3.5 0 017 0v3" fill="none" stroke="#6b449b" stroke-width="1.6"/></svg>
  </div>
  <p class="abs lead" style="top:136px">Lorem Ipsum is simply dummy text of the printing and typesetting industry. Lorem Ipsum has been the industry's standard dummy text ever since the 1500s, when an unknown printer took a galley of type and scrambled it.</p>

  <div class="abs member" style="left:173px">
    <div class="member__photo" role="img" aria-label="Portrait photo of a smiling team member holding a coffee cup" style="background:radial-gradient(ellipse 70px 85px at 55% 38%,rgba(205,160,130,.85) 0,rgba(205,160,130,0) 100%),radial-gradient(ellipse 120px 70px at 50% 100%,rgba(35,35,40,1) 0,rgba(35,35,40,0) 100%),linear-gradient(180deg,#f4f4f4 0%,#ebe9e7 50%,#56565c 100%)"></div>
    <h4>ALDO RENFRY</h4><p>Lorem Ipsum is simply</p>
  </div>
  <div class="abs member" style="left:392px">
    <div class="member__photo" role="img" aria-label="Portrait photo of a smiling team member in a blue jacket" style="background:radial-gradient(ellipse 75px 95px at 50% 36%,rgba(190,140,110,.8) 0,rgba(120,80,55,.45) 60%,rgba(0,0,0,0) 100%),radial-gradient(ellipse 120px 70px at 50% 100%,rgba(26,56,130,1) 0,rgba(26,56,130,0) 100%),linear-gradient(180deg,#f2f2f2 0%,#e8e6e4 55%,#294a96 100%)"></div>
    <h4>CELIA VANTOR</h4><p>Lorem Ipsum is simply</p>
  </div>
  <div class="abs member" style="left:611px">
    <div class="member__photo" role="img" aria-label="Portrait photo of a team member" style="background:radial-gradient(ellipse 70px 90px at 50% 40%,rgba(180,150,130,.7) 0,rgba(0,0,0,0) 100%),linear-gradient(180deg,#d8d8d8,#8a8a8a 60%,#2a2a2a)"></div>
    <div class="member__over">
      <h4>BRAM HOLLIS</h4><p>Lorem Ipsum is simply</p>
      <div class="social"><span></span><span></span><span></span><span></span><span></span></div>
    </div>
  </div>
  <div class="abs member" style="left:829px">
    <div class="member__photo" role="img" aria-label="Portrait photo of a team member with long light brown hair" style="background:radial-gradient(ellipse 60px 80px at 50% 38%,rgba(225,185,160,.85) 0,rgba(0,0,0,0) 100%),radial-gradient(ellipse 100px 150px at 50% 55%,rgba(150,115,85,.6) 0,rgba(0,0,0,0) 100%),linear-gradient(180deg,#ecebea 0%,#d9d3cd 50%,#9d8672 100%)"></div>
    <h4>INES MARLOW</h4><p>Lorem Ipsum is simply</p>
  </div>
</section>

<!-- footer -->
<footer class="block footer">
  <h3 class="abs" style="left:173px">ABOUT US</h3>
  <p class="abs" style="left:173px;top:80px;width:262px">Lorem ipsum dolor sit amet, consectetuer adipiscing elit, sed diam nonummy nibh euismod tincidunt laoreet dolore magna aliquam.</p>
  <div class="abs social" style="left:173px;top:154px"><span></span><span></span><span></span><span></span><span></span></div>

  <h3 class="abs" style="left:475px">LATEST NEWS</h3>
  <div class="abs news" style="left:475px;top:80px;width:270px">
    <div class="date">12<small>DEC</small></div>
    <p>Claritas est etiam processus dynamicus, qui sequitur mutationem consuetudium <em>26 COMMENTS</em></p>
  </div>
  <div class="abs news" style="left:475px;top:170px;width:270px">
    <div class="date">10<small>DEC</small></div>
    <p>Claritas est etiam processus dynamicus, qui sequitur mutationem consuetudium <em>26 COMMENTS</em></p>
  </div>

  <h3 class="abs" style="left:775px">GET IN TOUCH</h3>
  <div class="abs addr" style="left:775px;top:76px;width:260px">
    <span>Address :</span><span>48 Harlow Crescent, Unit 3<br>Fenwick, QN 4410, Australia</span>
    <span>Phone :</span><span>+440 870555214</span>
    <span>Email :</span><span>info@dalmorenvue.com</span>
  </div>
</footer>

<div class="block bottombar">
  <p class="abs">© 2018 DALMOREN VUE . ALL RIGHT RESERVED.</p>
  <ul><li>HOME</li><li>OUR TEAM</li><li>SERVICES</li><li>PRODUCT</li><li>CONTACT US</li></ul>
</div>

</body>
</html>
```